Torvessa Plates App UI Mockup

Hey Freelance I need this to be tasteful.
Best design wins!
The design and colour scheme needs to be sleek, clean and modern.
Torvessa Plates App (Sacramento Font) Only for app Name (File attached with colour)
Social and GPS Navigation Platform
Requires an Icon
This app will have GPS navigation (In each restaurant profile) How to get around to the restaurants in Anguilla
Has to be able to link to chatterlo for sign in so that users can interact with friends that travel to Anguilla
Must have sign up page (Used chatterlo to sign up) or email and password
Restaurants Profile will have basic information, (cuisine types, phone number, email,Map) User comments will be below. The profile pic will sure how many persons loved or passed. below the pic.
It will have a Social feed where guess will upload pictures of their food at which ever restaurant and it post under a general feed where all users can (Love or Pass) the post and/or comment. (Picture and video post)
The home screen will be split in half. Upper half, image of food to choose from (Love or Pass) – When you click love or pass it will take you into another screen that allows you to vote on all the other pictures uploaded by other users.
Lower half will have what’s listed below.
Main Category (Dont write Main Category)
Restaurants
--------------------- (Put something that separates)
Resources (This is not a clickable Tab)
---------------------------------------------------------------------
Accomodations (List) Inn, Hotel, Villa -----> Picture feed that scrolls down.
Transportation (List) Air,Sea,Land -----> Picture feed that scrolls down.
Things to do (List) ---------------------> Picture feed that scrolls down.
Faqs
The selected Freelancer might still need to work with me until [login to view URL] feel free to let me know if you need more information.

```html
<!DOCTYPE html>
<html lang="en">
<head>
<meta charset="UTF-8">
<title>Torvessa Plates – Home</title>
<link rel="stylesheet" href="https://fonts.googleapis.com/css2?family=Montserrat:wght@500;600;700&display=swap">
<style>
  :root {
    --ink: #25282b;
    --accent: #3ad6e8;
    --white: #ffffff;
    --muted: #d4d6d8;
    --photo-top: #b89a7c;
    --photo-mid: #8a5a36;
    --photo-low: #d9d4cc;
    --veil: #0f4a4f;
  }
  * { margin: 0; padding: 0; box-sizing: border-box; }
  html, body { width: 1200px; height: 2250px; overflow: hidden; background: var(--ink); }
  body { font-family: "Montserrat", sans-serif; color: var(--white); position: relative; }

  .app-header { position: absolute; left: 0; top: 0; width: 1200px; height: 250px; background: var(--ink); }
  .menu-toggle { position: absolute; left: 63px; top: 105px; width: 84px; height: 72px; }
  .app-title { position: absolute; left: 0; right: 0; top: 108px; text-align: center; font-weight: 500; font-size: 64px; color: var(--accent); letter-spacing: 1px; }
  .add-post { position: absolute; left: 1070px; top: 105px; width: 80px; height: 80px; }

  .feed-card { position: absolute; left: 0; top: 250px; width: 1200px; height: 917px; }
  .feed-photo { position: absolute; inset: 0;
    background:
      linear-gradient(180deg, rgba(15,74,79,0) 68%, rgba(15,74,79,.85) 100%),
      radial-gradient(ellipse 55% 45% at 42% 55%, var(--photo-mid) 0%, rgba(138,90,54,0) 100%),
      radial-gradient(ellipse 30% 30% at 85% 62%, #c8692c 0%, rgba(200,105,44,0) 100%),
      linear-gradient(180deg, var(--photo-top) 0%, #9e8a74 40%, var(--photo-low) 75%, #7b8f8c 100%);
  }
  .poster-avatar { position: absolute; left: 63px; top: 314px; width: 240px; height: 240px; border-radius: 50%; background: #d8d2cb; }
  .poster-name { position: absolute; left: 348px; top: 362px; font-weight: 700; font-size: 54px; color: var(--white); }
  .feed-actions { position: absolute; left: 0; top: 740px; width: 1200px; height: 180px; }
  .action-love { position: absolute; left: 62px; top: 250px; }
  .action-comment { position: absolute; left: 576px; top: 286px; }
  .action-pass { position: absolute; left: 1063px; top: 285px; }

  .home-links { position: absolute; left: 0; top: 1167px; width: 1200px; }
  .section-label { position: absolute; font-weight: 700; font-size: 62px; color: var(--accent); white-space: nowrap; }
  .nav-link { position: absolute; font-weight: 500; font-size: 51px; color: var(--white); text-decoration: none; white-space: nowrap; border-bottom: 2px solid var(--white); line-height: 1.1; padding-bottom: 2px; }

  .app-footer { position: absolute; left: 0; right: 0; top: 2125px; text-align: center; font-weight: 500; font-size: 46px; color: var(--muted); margin-left: -30px; }
</style>
</head>
<body>
  <header class="app-header">
    <svg class="menu-toggle" viewBox="0 0 84 72" aria-label="Menu">
      <rect x="0" y="0" width="84" height="12" fill="#fff"/>
      <rect x="0" y="30" width="84" height="12" fill="#fff"/>
      <rect x="0" y="60" width="84" height="12" fill="#fff"/>
    </svg>
    <div class="app-title">Torvessa Plates</div>
    <svg class="add-post" viewBox="0 0 80 80" aria-label="Add post">
      <circle cx="40" cy="40" r="34" fill="none" stroke="#fff" stroke-width="7"/>
      <path d="M40 22v36M22 40h36" stroke="#fff" stroke-width="7" stroke-linecap="round"/>
    </svg>
  </header>

  <div class="feed-photo" role="img" aria-label="Photo of a burger with greens, mushrooms and cheese beside roasted sweet potato cubes" style="top:250px;height:917px;position:absolute;left:0;width:1200px;"></div>

  <div class="poster-avatar" role="img" aria-label="Profile photo of the poster"></div>
  <div class="poster-name">jonno451</div>

  <svg class="action-love" style="position:absolute;left:62px;top:990px" width="140" height="132" viewBox="0 0 140 132" aria-label="Love">
    <path d="M70 124 L14 64 C-6 42 8 8 38 8 C54 8 64 18 70 28 C76 18 86 8 102 8 C132 8 146 42 126 64 Z" fill="none" stroke="#3ad6e8" stroke-width="7" stroke-linejoin="round"/>
  </svg>
  <svg class="action-comment" style="position:absolute;left:576px;top:1036px" width="110" height="92" viewBox="0 0 110 92" aria-label="Comment">
    <path d="M14 4 H96 A10 10 0 0 1 106 14 V56 A10 10 0 0 1 96 66 H36 L18 86 V66 H14 A10 10 0 0 1 4 56 V14 A10 10 0 0 1 14 4 Z" fill="none" stroke="#fff" stroke-width="5" stroke-linejoin="round"/>
  </svg>
  <svg class="action-pass" style="position:absolute;left:1063px;top:1035px" width="86" height="86" viewBox="0 0 86 86" aria-label="Pass">
    <path d="M6 8 H44 C56 8 70 12 76 16 C82 20 82 26 78 30 C84 34 84 40 78 44 C84 48 82 56 76 58 C80 62 78 68 70 70 H46 L50 80 C52 86 42 88 38 80 L22 58 H6 Z" fill="none" stroke="#fff" stroke-width="5" stroke-linejoin="round"/>
    <path d="M22 10 V58" stroke="#fff" stroke-width="5"/>
  </svg>

  <nav class="home-links" aria-label="Home navigation">
    <div class="section-label" style="left:95px;top:83px">Restaurants</div>
    <a class="nav-link" href="#" style="left:604px;top:133px">View More</a>
    <div class="section-label" style="left:97px;top:358px">Resources</div>
    <a class="nav-link" href="#" style="left:592px;top:423px">Accommodation</a>
    <a class="nav-link" href="#" style="left:597px;top:573px">Things To Do</a>
    <a class="nav-link" href="#" style="left:603px;top:720px">FAQ</a>
  </nav>

  <footer class="app-footer">Torvessa Plates</footer>
</body>
</html>
```